Camp Thornbrake "The '63 Circle"

We are looking for someone to design a bi-fold brochure that will help with our fundraising program. We are a Christian camp and retreat center. It would be a good idea to visit our website to get a feel for what we do, campthornbrake.org.

This link, https://files.exampleshare.net/folders/9KxTb3RmQa7VzLp2NcHw5YdFs8GjUe4Xo?usp=sharing, will provide you with pictures you can use and the text that will be needed. Don't expect all the pictures to be used, but wanted to provide some choices. The text that is provided will need to be used on the inside portion of the brochure.

Target Market(s)

Donors age range 25-70

Industry/Entity Type

Recreation

Requirements
Must have
• Text included in Google Drive. A few pictures. Thornbrake Logo
Nice to have
• Professional Design
Should not have
• No clip art, no extra text (even from the website)

```html
<!DOCTYPE html>
<html lang="en">
<head>
<meta charset="utf-8">
<title>Camp Thornbrake – The '63 Circle Brochure</title>
<link rel="stylesheet" href="https://fonts.googleapis.com/css2?family=Oswald:wght@500;700&family=Open+Sans:wght@400;600;700&display=swap">
<style>
  :root{
    --green:#1e7a4c;
    --green-dark:#165c39;
    --orange:#f08a24;
    --white:#ffffff;
    --ink:#4a4a4a;
    --stage:#e6e6e6;
  }
  *{box-sizing:border-box;margin:0;padding:0}
  html,body{width:1200px;height:3196px;overflow:hidden}
  body{background:var(--stage);font-family:"Open Sans",Arial,sans-serif;color:var(--ink);position:relative}

  .panel,.spread{position:absolute;background:var(--white);overflow:hidden;box-shadow:0 6px 24px rgba(0,0,0,.12)}
  .cover-panel{left:250px;top:200px;width:700px;height:906px}
  .spread{left:50px;width:1100px;height:712px}
  .spread--inside{top:1322px}
  .spread--outside{top:2250px}

  .shapes{position:absolute;inset:0;width:100%;height:100%}
  .photo{position:absolute}

  .brand-badge{position:absolute;border-radius:50%;background:var(--white);border:5px solid var(--green);
    display:flex;align-items:center;justify-content:center;text-align:center;
    font-family:"Oswald",sans-serif;font-weight:700;color:var(--green);text-transform:uppercase;line-height:1.05}
  .cover-title{position:absolute;font-family:"Oswald",sans-serif;font-weight:700;color:var(--green);
    text-transform:uppercase;text-align:center;line-height:1.05;letter-spacing:.3px;white-space:nowrap}
  .url-pill{position:absolute;background:var(--orange);color:var(--white);border-radius:40px;
    font-weight:600;text-align:center;font-family:"Open Sans",sans-serif}

  /* cover */
  .cover-panel .photo{left:0;top:0;width:700px;height:560px;
    background:linear-gradient(160deg,#6f8f5a 0%,#b79a6e 45%,#5b7a48 100%)}
  .cover-panel .brand-badge{left:275px;top:435px;width:150px;height:150px;font-size:22px}
  .cover-panel .cover-title{left:30px;width:640px;top:612px;font-size:40px}
  .cover-panel .url-pill{left:200px;width:300px;top:730px;height:44px;line-height:44px;font-size:18px}

  /* inside spread */
  .about{position:absolute;left:48px;top:44px;width:460px}
  .section-title{font-family:"Oswald",sans-serif;font-weight:700;color:var(--green);font-size:30px;
    text-transform:uppercase;letter-spacing:.5px}
  .section-title::after{content:"";display:block;width:70px;height:4px;background:var(--orange);margin-top:4px}
  .body-copy{font-size:12.5px;line-height:1.6;margin-top:14px}
  .callout{font-family:"Oswald",sans-serif;font-weight:500;color:var(--orange);font-size:19px;line-height:1.3;margin-top:16px}
  .spread--inside .url-pill{left:48px;top:598px;width:230px;height:36px;line-height:36px;font-size:14px}

  .circle-photo{position:absolute;border-radius:50%;border:6px solid var(--white);box-shadow:0 0 0 3px var(--green)}
  .circle-photo--large{left:820px;top:70px;width:240px;height:240px;background:linear-gradient(150deg,#3f7fb0,#e2a64a 55%,#4e8a4f)}
  .circle-photo--medium{left:660px;top:60px;width:170px;height:170px;background:linear-gradient(140deg,#d07a3a,#6a9a5a)}
  .circle-photo--small{left:720px;top:220px;width:120px;height:120px;background:linear-gradient(150deg,#4b9bc8,#c9d9e6)}
  .circle-club{position:absolute;left:600px;top:350px;width:450px}

  /* outside spread */
  .spread--outside .photo--history{left:0;top:0;width:560px;height:440px;background:linear-gradient(135deg,#5b5b5b,#b4b4b4 55%,#7a7a7a)}
  .spread--outside .photo--campers{left:560px;top:0;width:540px;height:440px;background:linear-gradient(160deg,#587a3f,#c7a26c 50%,#3f6a38)}
  .contact{position:absolute;left:40px;top:510px;color:var(--white)}
  .contact h3{font-family:"Oswald",sans-serif;font-weight:700;font-size:24px;letter-spacing:.5px;text-transform:uppercase}
  .contact-line{display:flex;align-items:center;gap:8px;font-size:12.5px;margin-top:8px}
  .contact-line svg{width:14px;height:14px;flex:none}
  .spread--outside .brand-badge{left:755px;top:380px;width:120px;height:120px;font-size:17px;border-width:4px}
  .spread--outside .cover-title{left:570px;width:500px;top:515px;font-size:32px}
  .spread--outside .url-pill{left:700px;width:240px;top:608px;height:34px;line-height:34px;font-size:14px}
</style>
</head>
<body>

<!-- Front cover -->
<section class="panel cover-panel">
  <div class="photo" role="img" aria-label="Photo of smiling campers outdoors under trees"></div>
  <svg class="shapes" viewBox="0 0 700 906" aria-hidden="true">
    <path d="M0 470 C180 530 420 420 700 470 L700 484 C420 436 180 546 0 486 Z" fill="var(--orange)"/>
    <path d="M0 492 C180 552 420 444 700 486 L700 540 C450 490 200 600 0 560 Z" fill="var(--green)"/>
    <path d="M0 560 C200 600 450 490 700 540 L700 906 L0 906 Z" fill="var(--white)"/>
    <path d="M0 830 C250 790 450 860 700 805 L700 906 L0 906 Z" fill="var(--orange)"/>
    <path d="M0 852 C250 815 450 885 700 832 L700 906 L0 906 Z" fill="var(--green)"/>
  </svg>
  <div class="brand-badge">Camp<br>Thornbrake</div>
  <h1 class="cover-title">Christian Camp<br>and Retreat Center Facility</h1>
  <div class="url-pill">www.campthornbrake.org</div>
</section>

<!-- Inside spread -->
<section class="spread spread--inside">
  <svg class="shapes" viewBox="0 0 1100 712" aria-hidden="true">
    <path d="M0 640 C120 600 260 660 400 712 L0 712 Z" fill="var(--green)"/>
    <path d="M0 612 C140 580 280 640 430 712 L412 712 C270 648 130 596 0 626 Z" fill="var(--orange)"/>
    <path d="M1100 0 L900 0 C960 40 1040 40 1100 90 Z" fill="var(--green)"/>
    <path d="M870 0 L884 0 C950 52 1040 56 1100 110 L1100 124 C1030 66 940 62 870 0 Z" fill="var(--orange)"/>
    <path d="M1100 660 C1000 640 900 690 820 712 L1100 712 Z" fill="var(--green)"/>
    <path d="M1100 640 C990 622 890 676 790 712 L808 712 C900 684 1000 636 1100 652 Z" fill="var(--orange)"/>
  </svg>

  <article class="about">
    <h2 class="section-title">About Thornbrake</h2>
    <p class="body-copy">Camp Thornbrake was established in 1963 by Walt and Edna Pruitt, who believed every child deserved a week outdoors among caring Christian mentors. For more than sixty years, families across the region have trusted us to offer a safe place to grow in faith, friendship and fun.</p>
    <p class="body-copy">We are committed to continuing that same core value. We don't believe an incredible camp experience should only be for kids who can afford it, so we keep our rates well below cost.</p>
    <p class="callout">It cost Thornbrake just over $300 for a one week camper and around $800 for a two week camper. We currently charge $285 for a one week session and $425.</p>
    <p class="body-copy">For a one week session, these gaps create a significant budget shortfall each year that must be filled with faithful gifts, grants and fundraising, which makes it challenging to plan new ministry and facility improvements.</p>
  </article>
  <div class="url-pill">www.campthornbrake.org</div>

  <div class="circle-photo circle-photo--large" role="img" aria-label="Photo of campers in life jackets by the lake"></div>
  <div class="circle-photo circle-photo--medium" role="img" aria-label="Photo of campers gathered at an activity"></div>
  <div class="circle-photo circle-photo--small" role="img" aria-label="Photo of campers on the water"></div>

  <article class="circle-club">
    <h2 class="section-title">The '63 Circle</h2>
    <p class="body-copy">In an effort to keep camper fees at a reasonable level we established The '63 Circle. Members of The '63 Circle are former campers, counselors and friends whose lives have been shaped by the ministry of Camp Thornbrake. By pledging a monthly gift, they help close the gap for every family we serve.</p>
    <p class="body-copy">We hope you will consider joining this effort. Recurring donations can be set up at campthornbrake.org by clicking the Give Now button at the top of the page and selecting The '63 Circle. Checks may also be mailed to P.O. Box 482, Linwood, AR 72199.</p>
  </article>
</section>

<!-- Outside spread -->
<section class="spread spread--outside">
  <div class="photo photo--history" role="img" aria-label="Historic black and white photo of the camp lodge with campers"></div>
  <div class="photo photo--campers" role="img" aria-label="Photo of campers standing together in the woods"></div>
  <svg class="shapes" viewBox="0 0 1100 712" aria-hidden="true">
    <path d="M0 400 C220 450 600 360 1100 420 L1100 434 C600 376 220 466 0 416 Z" fill="var(--orange)"/>
    <path d="M0 420 C220 470 600 380 1100 438 L1100 470 C700 420 300 500 0 460 Z" fill="var(--green)"/>
    <path d="M0 460 C300 500 700 420 1100 470 L1100 712 L0 712 Z" fill="var(--white)"/>
    <path d="M0 470 C160 500 380 470 550 490 L550 712 L0 712 Z" fill="var(--green)"/>
    <path d="M550 665 C750 640 900 690 1100 655 L1100 712 L550 712 Z" fill="var(--orange)"/>
    <path d="M550 682 C750 660 900 705 1100 676 L1100 712 L550 712 Z" fill="var(--green)"/>
  </svg>

  <div class="contact">
    <h3>Contact Us</h3>
    <p class="contact-line">
      <svg viewBox="0 0 24 24"><path fill="#fff" d="M6.6 10.8a15 15 0 0 0 6.6 6.6l2.2-2.2c.3-.3.7-.4 1-.2 1.1.4 2.3.6 3.6.6.6 0 1 .4 1 1V20c0 .6-.4 1-1 1A17 17 0 0 1 3 4c0-.6.4-1 1-1h3.5c.6 0 1 .4 1 1 0 1.3.2 2.5.6 3.6.1.3 0 .7-.2 1z"/></svg>
      501-555-0148
    </p>
    <p class="contact-line">
      <svg viewBox="0 0 24 24"><path fill="#fff" d="M2 5h20v14H2z M2 5l10 8 10-8" stroke="#1e7a4c" stroke-width="1.5"/></svg>
      office@campthornbrake.org
    </p>
    <p class="contact-line">
      <svg viewBox="0 0 24 24"><path fill="#fff" d="M12 2a7 7 0 0 0-7 7c0 5 7 13 7 13s7-8 7-13a7 7 0 0 0-7-7zm0 9.5A2.5 2.5 0 1 1 12 6.5a2.5 2.5 0 0 1 0 5z"/></svg>
      118 Cedar Hollow Road, Linwood, AR 72199
    </p>
  </div>

  <div class="brand-badge">Camp<br>Thornbrake</div>
  <h2 class="cover-title">Christian Camp<br>and Retreat Center Facility</h2>
  <div class="url-pill">www.campthornbrake.org</div>
</section>

</body>
</html>
```